Energieausweis
Zielgruppe
Zielgruppe sind Immobilieninteressenten - Verwendung in einem Immobilienmagazin und im Internet.
Aufgabenstellung
Ab dem 1. Mai muss in Deutschland die Energie-Effizienzklasse bei Immobilienangeboten mit veröffentlicht werden. Das kann man nüchtern in Zahlen darstellen, aber auch in einer netten Grafik. In der Anlage finden 2 von uns gekaufte Vorimka-Bilder. Das Bild mit dem Männchen ist eine sehr nette Idee. Da wir in unserem Logo auch ein Männchen haben, bietet es sich an, ein TalwiesenHof-Männchen zusammen mit der bunten Grafik zu gestalten. (Das Vorimka-Bild soll nur die Idee erklären - bitte nicht verwenden). Wenn die Grafik fertig ist, legen wir einen Pfeil zur Kennzeichnung der jeweiligen Energieklasse hinzu. Das heisst, wir haben dann für jede Energieklasse eine entsprechende Vorlage und dem richtig platzierten Pfeil. Weiter finden sie in der Anlage unser Firmenlogo zur freuen Verwendung.

```html
<!DOCTYPE html>
<html lang="de">
<head>
<meta charset="utf-8">
<title>Energieausweis – TalwiesenHof</title>
<link rel="stylesheet" href="https://fonts.googleapis.com/css2?family=Fira+Sans+Condensed:wght@600&family=PT+Sans:wght@400;700&family=Arimo:wght@400;700&display=swap">
<style>
  :root {
    --page-bg: #ececec;
    --panel-bg: #e3e3e3;
    --band-bg: #cfcfcf;
    --frame-blue: #1f5ea8;
    --brand-navy: #1e4f93;
    --title-red: #d7193a;
    --text-dark: #2b2b2b;
  }
  * { box-sizing: border-box; margin: 0; padding: 0; }
  html, body { width: 1200px; height: 682px; overflow: hidden; }
  body { background: var(--page-bg); position: relative; font-family: "PT Sans", sans-serif; }

  .brand-box {
    position: absolute; top: 19px; width: 316px; height: 101px;
    background: #e6e6e6;
    display: flex; align-items: center; justify-content: center; gap: 12px;
  }
  .brand-mark { width: 22px; height: 22px; border-radius: 50%; background: var(--title-red); }
  .brand-name {
    font-family: "Fira Sans Condensed", sans-serif; font-weight: 600;
    font-size: 36px; color: var(--brand-navy); letter-spacing: 0.2px;
  }

  .label-panel {
    position: absolute; top: 133px; width: 316px; height: 416px;
    background: var(--panel-bg);
  }
  .label-panel.compact { height: 404px; }
  .label-title {
    position: absolute; left: 11px; top: 12px; width: 291px; height: 49px;
    border: 2.5px solid var(--frame-blue); border-radius: 6px; background: #efefef;
    display: flex; align-items: center; justify-content: center;
    font-family: "Fira Sans Condensed", sans-serif; font-weight: 600;
    font-size: 33px; color: var(--title-red); letter-spacing: 0.6px;
  }
  .label-subtitle {
    position: absolute; left: 11px; top: 69px; width: 291px; height: 37px;
    background: var(--band-bg); padding-left: 12px;
    display: flex; align-items: center;
    font-size: 17px; color: var(--text-dark); letter-spacing: 0.3px;
  }
  .label-scale { position: absolute; left: 11px; top: 113px; width: 291px; height: 289px; }

  .legend-box {
    position: absolute; left: 821px; top: 562px; width: 316px; height: 101px;
    background: #e6e6e6;
  }
</style>
</head>
<body>

<svg width="0" height="0" style="position:absolute">
  <defs>
    <filter id="marker-shadow" x="-20%" y="-20%" width="150%" height="150%">
      <feDropShadow dx="2" dy="2" stdDeviation="1.5" flood-opacity="0.35"/>
    </filter>
    <g id="class-bars">
      <rect x="2" y="2" width="456" height="454" rx="12" fill="#e9e9e9" stroke="#1f5ea8" stroke-width="4"/>
      <polygon points="20,19 140,19 180,44 140,69 20,69" fill="#006a2f"/>
      <polygon points="20,80.6 180,80.6 220,105.6 180,130.6 20,130.6" fill="#23a12f"/>
      <polygon points="20,142.2 220,142.2 260,167.2 220,192.2 20,192.2" fill="#9dc00f"/>
      <polygon points="20,203.8 260,203.8 300,228.8 260,253.8 20,253.8" fill="#e2dc0a"/>
      <polygon points="20,265.4 300,265.4 340,290.4 300,315.4 20,315.4" fill="#edbb00"/>
      <polygon points="20,327 340,327 380,352 340,377 20,377" fill="#ea7700"/>
      <polygon points="20,388.6 380,388.6 420,413.6 380,438.6 20,438.6" fill="#e12323"/>
    </g>
    <g id="class-letters" font-family="Arimo, sans-serif" font-weight="700" font-size="34" fill="#ffffff">
      <text x="36" y="57">A</text>
      <text x="36" y="118.6">B</text>
      <text x="36" y="180.2">C</text>
      <text x="36" y="241.8">D</text>
      <text x="36" y="303.4">E</text>
      <text x="36" y="365">F</text>
      <text x="36" y="426.6">G</text>
    </g>
    <g id="class-values" font-family="Arimo, sans-serif" font-weight="400" font-size="16" fill="#ffffff">
      <text x="91" y="51">50 <tspan font-size="12">kw/h</tspan></text>
      <text x="81" y="112.6">100 <tspan font-size="12">kw/h</tspan></text>
      <text x="81" y="174.2">150 <tspan font-size="12">kw/h</tspan></text>
      <text x="81" y="235.8">200 <tspan font-size="12">kw/h</tspan></text>
      <text x="81" y="297.4">300 <tspan font-size="12">kw/h</tspan></text>
      <text x="81" y="359">400 <tspan font-size="12">kw/h</tspan></text>
      <text x="71" y="420.6">&gt;400 <tspan font-size="12">kw/h</tspan></text>
    </g>
  </defs>
</svg>

<!-- Variant 1: class B with values -->
<section class="label-panel" style="left:64px">
  <h2 class="label-title">ENERGIEAUSWEIS</h2>
  <p class="label-subtitle">Berechneter Energiebedarf</p>
  <svg class="label-scale" viewBox="0 0 460 458" aria-label="Energieklassen A bis G, markiert: B">
    <use href="#class-bars"/><use href="#class-letters"/><use href="#class-values"/>
    <g class="class-marker" filter="url(#marker-shadow)">
      <polygon points="160,105 222,98 222,112" fill="#fff"/>
      <rect x="222" y="78" width="60" height="52" fill="#fff"/>
    </g>
    <circle cx="252" cy="104" r="13" fill="#1e4f93"/>
  </svg>
</section>

<!-- Variant 2: class D with values -->
<header class="brand-box" style="left:442px">
  <span class="brand-mark"></span><span class="brand-name">TalwiesenHof</span>
</header>
<section class="label-panel" style="left:442px">
  <h2 class="label-title">ENERGIEAUSWEIS</h2>
  <p class="label-subtitle">Berechneter Energiebedarf</p>
  <svg class="label-scale" viewBox="0 0 460 458" aria-label="Energieklassen A bis G, markiert: D">
    <use href="#class-bars"/><use href="#class-letters"/><use href="#class-values"/>
    <g class="class-marker" filter="url(#marker-shadow)">
      <polygon points="240,230 301,223 301,237" fill="#fff"/>
      <rect x="301" y="203" width="61" height="52" fill="#fff"/>
    </g>
    <circle cx="331" cy="229" r="13" fill="#1e4f93"/>
  </svg>
</section>

<!-- Variant 3: class F, letters only -->
<header class="brand-box" style="left:821px">
  <span class="brand-mark"></span><span class="brand-name">TalwiesenHof</span>
</header>
<section class="label-panel compact" style="left:821px">
  <h2 class="label-title">ENERGIEAUSWEIS</h2>
  <p class="label-subtitle">Berechneter Energiebedarf</p>
  <svg class="label-scale" viewBox="0 0 460 458" aria-label="Energieklassen A bis G, markiert: F">
    <use href="#class-bars"/><use href="#class-letters"/>
    <g class="class-marker" filter="url(#marker-shadow)">
      <polygon points="320,354 382,347 382,361" fill="#fff"/>
      <rect x="382" y="327" width="60" height="52" fill="#fff"/>
    </g>
    <circle cx="412" cy="353" r="13" fill="#1e4f93"/>
  </svg>
</section>

<aside class="legend-box">
  <svg viewBox="0 0 500 160" width="316" height="101" aria-label="Legende der Energieklassen in kw/h">
    <g stroke="#fff" stroke-width="2">
      <rect x="22" y="20" width="52" height="52" fill="#006a2f"/>
      <rect x="138" y="20" width="52" height="52" fill="#23a12f"/>
      <rect x="254" y="20" width="52" height="52" fill="#9dc00f"/>
      <rect x="370" y="20" width="52" height="52" fill="#e2dc0a"/>
      <rect x="22" y="90" width="52" height="52" fill="#edbb00"/>
      <rect x="138" y="90" width="52" height="52" fill="#ea7700"/>
      <rect x="254" y="90" width="52" height="52" fill="#e12323"/>
    </g>
    <g font-family="Arimo, sans-serif" font-weight="700" font-size="34" fill="#fff" text-anchor="middle">
      <text x="48" y="58">A</text><text x="164" y="58">B</text>
      <text x="280" y="58">C</text><text x="396" y="58">D</text>
      <text x="48" y="128">E</text><text x="164" y="128">F</text>
      <text x="280" y="128">G</text>
    </g>
    <g font-family="Arimo, sans-serif" font-size="20" fill="#2b2b2b" text-anchor="middle">
      <text x="106" y="53">50</text><text x="222" y="53">100</text>
      <text x="338" y="53">150</text><text x="454" y="53">200</text>
      <text x="106" y="123">300</text><text x="222" y="123">400</text>
      <text x="338" y="123">&gt;400</text>
    </g>
    <text x="434" y="127" font-family="Arimo, sans-serif" font-size="34" fill="#2b2b2b" text-anchor="middle">kw/h</text>
  </svg>
</aside>

</body>
</html>
```